Website for AV installation with booking system and e-commerce

Company: Corvexa
Tag Line: Audio Visual and Security System Installations
We need a website for an AV company based in Sydney Australia. We specialise in Audio Visual, CCTV (security cameras), and Data Cabling.
The purpose of the website is that customers book their installation online with a live booking system.
We are looking for the following:
- Creative and modern design
- easy to use - keep in mind that the user who will book will have little knowledge in technology.
- clean and organised
- colours to work in well with our logo we also like royal to navy blue, but we are open to other suggested what works well with our logo.
We want customers to be able to add products needed for their installation ie when booking to wall mount their TV they can choose to add a TV bracket and cables to the cart and vise-versa buy a bracket or cables and add to cart the installation.
Tabs to be included:
About us
Gallery
Contact Us
Home
Services (there are three services that we offer - Residential, Corporate and Retail)
Products
Book Online/Cart (checkout)
Temporary website checkout: www.corvexa.com.au, please note this is very basic and we do not want a copy of this. This is purely to give you an idea of our company.
Good Luck!
Target Market(s)
home owners/renters, business owners, archiects/designers, builders
Industry/Entity Type
E-Commerce
Look and feel

```html
<!DOCTYPE html>
<html lang="en">
<head>
<meta charset="utf-8">
<title>Corvexa – Audio Visual and Security System Installations</title>
<link href="https://fonts.googleapis.com/css2?family=Source+Sans+3:wght@400;600&display=swap" rel="stylesheet">
<style>
:root{
  --red:#d40d12;
  --red-dark:#a8080c;
  --ink:#333;
  --muted:#555;
  --nav:#1e1e1e;
  --band:#e9e9e9;
  --line:#d3d3d3;
  --white:#fff;
  --footer-top:#3b3b3b;
  --footer-bot:#0d0d0d;
}
*{box-sizing:border-box;margin:0;padding:0}
html,body{width:1200px;height:1137px;overflow:hidden;background:var(--white);font-family:"Source Sans 3",Arial,sans-serif;color:var(--ink)}
.page{position:relative;width:1200px;height:1137px}
.abs{position:absolute}

.topbar{left:0;top:0;width:1200px;height:28px;background:linear-gradient(#fafafa,#e6e6e6);border-bottom:1px solid #ccc}
.top-btn{top:3px;height:20px;background:#222;color:#fff;font-size:11px;border-radius:2px;display:flex;align-items:center;justify-content:center;gap:5px}

.brand{left:153px;top:44px;font-size:40px;font-weight:600;color:var(--red);letter-spacing:1px;display:flex;align-items:center;gap:10px;line-height:1}
.brand .dot{width:22px;height:22px;background:var(--red);border-radius:50%}

.search{left:894px;top:49px;width:152px;height:31px;border:1px solid #ccc;border-radius:3px;background:linear-gradient(#fff,#ececec);display:flex;align-items:center;gap:8px;padding-left:10px;font-size:11.5px;color:#333}

.mainnav{left:153px;top:103px;width:894px;height:31px;background:linear-gradient(#2d2d2d,#111);display:flex;border-radius:2px}
.mainnav a{color:#fff;text-decoration:none;font-size:11.5px;display:flex;align-items:center;justify-content:center;border-right:1px solid #444}
.mainnav a.active{background:var(--red);margin:0 6px 0 16px;border:none}

.band{left:0;top:148px;width:1200px;height:567px;background:var(--band)}

.hero{left:153px;top:160px;width:893px;height:341px;border:1px solid #ccc;background:linear-gradient(90deg,#fff 0%,#f4f4f4 45%,#eee 100%);overflow:hidden}
.hero .photo{position:absolute;left:380px;top:0;width:513px;height:341px;background:linear-gradient(120deg,#eef3ee 0%,#cfe3d0 30%,#f2f1c4 55%,#f0cccc 80%,#f5f5f5 100%)}
.hero h1{position:absolute;left:36px;top:42px;font-weight:400;font-size:40px;color:var(--red);letter-spacing:.5px}
.hero p{position:absolute;left:39px;top:99px;width:290px;font-size:12px;line-height:18.5px;color:#333}
.btn-red{background:var(--red);color:#fff;font-size:12px;border-radius:2px;display:flex;align-items:center;justify-content:center;box-shadow:0 1px 2px rgba(0,0,0,.3)}
.hero .read{position:absolute;left:40px;top:202px;width:75px;height:30px}
.dots{position:absolute;left:43px;top:288px;display:flex;gap:9px}
.dots span{width:15px;height:15px;border:1.3px solid #555;border-radius:50%;position:relative}
.dots span.on::after{content:"";position:absolute;left:4px;top:4px;width:5px;height:5px;background:var(--red);border-radius:50%}

.card{top:514px;height:187px;background:linear-gradient(#fff,#f3f3f3);border:1px solid var(--line)}
.card h2{position:absolute;left:16px;top:10px;font-weight:400;font-size:23px;color:var(--red)}
.card p{position:absolute;left:17px;top:41px;width:250px;font-size:12.5px;line-height:18.5px;color:#444}
.card .photo{position:absolute;left:8px;top:88px;width:180px;height:92px;border-radius:4px}
.card .more{position:absolute;right:3px;bottom:3px;width:62px;height:24px}

.section-title{font-weight:400;font-size:23px;color:var(--red)}
.arrow-btn{width:26px;height:26px;border-radius:50%;display:flex;align-items:center;justify-content:center}

.products{left:153px;top:771px;width:611px;height:191px;border:1px solid var(--line);background:#fff}
.product{position:absolute;top:13px;width:132px}
.product .thumb{width:132px;height:96px;background:#ddd;padding:6px}
.product .thumb div{width:100%;height:100%}
.product h3{font-weight:400;font-size:16px;color:var(--red);margin-top:10px}
.product p{font-size:11px;line-height:14px;color:#444;margin-left:2px;width:120px}
.cart{display:inline-flex;align-items:center;justify-content:center;margin:6px 0 0 2px;background:#222;color:#fff;font-size:11px;height:18px;padding:0 7px;border-radius:2px}

.svc{left:790px;width:252px;height:49px;background:linear-gradient(90deg,#f6f6f6,#e8e8e8);border:1px solid #ddd;display:flex;align-items:center}
.svc .ico{width:50px;display:flex;justify-content:center}
.svc .name{font-size:23px;color:#333;flex:1}
.svc .more{width:45px;height:24px;margin-right:14px}

.footer{left:153px;top:979px;width:894px;height:158px;background:linear-gradient(var(--footer-top),var(--footer-bot));border-radius:3px 3px 0 0;color:#fff;font-size:11.5px}
.footer .follow{position:absolute;left:22px;top:20px}
.socials{position:absolute;left:22px;top:41px;display:flex;gap:7px}
.socials span{width:19px;height:19px;border-radius:3px}
.contact{position:absolute;right:24px;top:20px;text-align:right;line-height:19px}
.footer hr{position:absolute;left:22px;right:22px;top:79px;border:none;border-top:1px solid #555}
.links{position:absolute;left:0;right:0;top:100px;text-align:center;line-height:19px}
.links span{margin:0 7px}
</style>
</head>
<body>
<div class="page">

  <div class="abs topbar"></div>
  <div class="abs top-btn" style="left:805px;width:109px">
    <svg width="13" height="11" viewBox="0 0 13 11"><path d="M0 1h2.5l2 6h6l1.5-4.5H4" fill="none" stroke="#fff" stroke-width="1.3"/><circle cx="5" cy="9.5" r="1.2" fill="#fff"/><circle cx="10" cy="9.5" r="1.2" fill="#fff"/></svg>Shopping Cart</div>
  <div class="abs top-btn" style="left:918px;width:54px">
    <svg width="9" height="11" viewBox="0 0 9 11"><rect x="0.5" y="4.5" width="8" height="6" fill="#fff"/><path d="M2 4.5V3a2.5 2.5 0 0 1 5 0v1.5" fill="none" stroke="#fff" stroke-width="1.3"/></svg>Login</div>
  <div class="abs top-btn" style="left:977px;width:64px">
    <svg width="10" height="11" viewBox="0 0 10 11"><circle cx="5" cy="3" r="2.5" fill="#fff"/><path d="M0 11c0-3.5 2-5 5-5s5 1.5 5 5z" fill="#fff"/></svg>Register</div>

  <div class="abs brand"><span class="dot"></span>Corvexa</div>

  <div class="abs search">
    <svg width="16" height="16" viewBox="0 0 16 16"><circle cx="6" cy="6" r="4.5" fill="none" stroke="#444" stroke-width="1.6"/><path d="M9.5 9.5l5 5" stroke="#444" stroke-width="2"/></svg>Search</div>

  <nav class="abs mainnav">
    <a class="active" href="#" style="width:80px">ABOUT US</a>
    <a href="#" style="width:121px">GALLERY</a>
    <a href="#" style="width:115px">CONTACT US</a>
    <a href="#" style="width:125px">HOME</a>
    <a href="#" style="width:132px">SERVICES</a>
    <a href="#" style="width:136px">PRODUCTS</a>
    <a href="#" style="width:143px;border:none">BOOK ONLINE/CART</a>
  </nav>

  <div class="abs band"></div>

  <section class="abs hero">
    <div class="photo" role="img" aria-label="Green, yellow and red network cables with plugs crossing"></div>
    <h1>DATA CABLING</h1>
    <p>Lorem Ipsum is simply dummy text of the printing and typesetting industry. Lorem Ipsum has been the industry's standard dummy text ever since the 1500s, when an unknown printer took a galley of type and scrambled</p>
    <div class="btn-red read">Read More</div>
    <div class="dots"><span></span><span class="on"></span><span></span><span></span></div>
  </section>

  <article class="abs card" style="left:153px;width:286px">
    <h2>Audio Visual</h2>
    <p>Lorem Ipsum is simply dummy text of the printing and typesetting&nbsp; Lorem Ipsum has</p>
    <div class="photo" role="img" aria-label="White video projector" style="background:linear-gradient(#f0f0f0,#c9c9c9)"></div>
    <div class="btn-red more">More &gt;&gt;</div>
  </article>
  <article class="abs card" style="left:456px;width:288px">
    <h2>CCTV</h2>
    <p>Lorem Ipsum is simply dummy text of the printing and typesetting&nbsp; Lorem Ipsum has</p>
    <div class="photo" role="img" aria-label="Wall-mounted security camera" style="width:165px;background:linear-gradient(#d8d8d8,#8e8e8e)"></div>
    <div class="btn-red more">More &gt;&gt;</div>
  </article>
  <article class="abs card" style="left:759px;width:287px">
    <h2>Data Cabling</h2>
    <p>Lorem Ipsum is simply dummy text of the printing and typesetting&nbsp; Lorem Ipsum has</p>
    <div class="photo" role="img" aria-label="Bundle of colourful network cables" style="left:0;width:150px;background:linear-gradient(120deg,#7cc47c,#f0d84a,#e86a3c,#b04ac0)"></div>
    <div class="btn-red more">More &gt;&gt;</div>
  </article>

  <h2 class="abs section-title" style="left:153px;top:735px">Feature Products</h2>
  <div class="abs arrow-btn" style="left:705px;top:736px;border:1px solid #999;background:#fff">
    <svg width="10" height="12" viewBox="0 0 10 12"><path d="M7 1L2 6l5 5" fill="none" stroke="#444" stroke-width="2"/></svg></div>
  <div class="abs arrow-btn" style="left:739px;top:736px;background:var(--red)">
    <svg width="10" height="12" viewBox="0 0 10 12"><path d="M3 1l5 5-5 5" fill="none" stroke="#fff" stroke-width="2"/></svg></div>

  <section class="abs products">
    <div class="product" style="left:10px">
      <div class="thumb"><div role="img" aria-label="Ceiling projector mount" style="background:linear-gradient(#c9ced6,#6f7782)"></div></div>
      <h3>Heading</h3><p>Lorem Ipsum is simply dummy text</p><span class="cart">Add to Cart</span>
    </div>
    <div class="product" style="left:161px">
      <div class="thumb"><div role="img" aria-label="Glowing audio video connectors" style="background:linear-gradient(120deg,#0a1a4a,#1c7a6a,#c0282a,#0a1a4a)"></div></div>
      <h3>Heading</h3><p>Lorem Ipsum is simply dummy text</p><span class="cart">Add to Cart</span>
    </div>
    <div class="product" style="left:316px">
      <div class="thumb"><div role="img" aria-label="SATA data cable" style="background:linear-gradient(#fff,#f3e0e0)"></div></div>
      <h3>Heading</h3><p>Lorem Ipsum is simply dummy text</p><span class="cart">Add to Cart</span>
    </div>
    <div class="product" style="left:467px">
      <div class="thumb"><div role="img" aria-label="Outdoor security camera" style="background:linear-gradient(#e6eaf0,#a9b2bd)"></div></div>
      <h3>Heading</h3><p>Lorem Ipsum is simply dummy text</p><span class="cart">Add to Cart</span>
    </div>
  </section>

  <h2 class="abs section-title" style="left:788px;top:735px">Our Services</h2>
  <div class="abs svc" style="top:780px">
    <div class="ico"><svg width="26" height="24" viewBox="0 0 26 24"><path d="M2 12L13 2l11 10" fill="none" stroke="#c8442a" stroke-width="2.5"/><rect x="5" y="11" width="16" height="12" fill="#f2e6cf" stroke="#b07a3a"/><rect x="11" y="15" width="5" height="8" fill="#c8442a"/></svg></div>
    <div class="name">Residential</div><div class="btn-red more">More</div>
  </div>
  <div class="abs svc" style="top:839px">
    <div class="ico"><svg width="26" height="26" viewBox="0 0 26 26"><circle cx="13" cy="8" r="6" fill="#e8c4a0"/><path d="M1 26c0-7 5-11 12-11s12 4 12 11z" fill="#2c3440"/><path d="M12 15h2l1 8-2 2-2-2z" fill="#1a4fa0"/></svg></div>
    <div class="name">Corporate</div><div class="btn-red more">More</div>
  </div>
  <div class="abs svc" style="top:900px">
    <div class="ico"><svg width="26" height="22" viewBox="0 0 26 22"><path d="M1 2h4l3 12h14l2-9H7" fill="none" stroke="#2a6fc4" stroke-width="2"/><circle cx="10" cy="18" r="2" fill="#2a6fc4"/><circle cx="20" cy="18" r="2" fill="#2a6fc4"/></svg></div>
    <div class="name">Retail</div><div class="btn-red more">More</div>
  </div>

  <footer class="abs footer">
    <div class="follow">Follow Us On</div>
    <div class="socials">
      <span style="background:#3b5aa0"></span><span style="background:#2a78b8"></span><span style="background:#3aa8e0"></span><span style="background:#f08a24"></span>
    </div>
    <div class="contact">Address, City, Street, Ph No: 444.XXX.XXXX<br>Email Id : info@companyname.com</div>
    <hr>
    <div class="links">About us<span>|</span>Gallery<span>|</span>Contact Us<span>|</span>Home<span>|</span>Services<span>|</span>Products<span>|</span>Book Online/Cart<br>Copyrights @ 2013 All Rights Reserved</div>
  </footer>

</div>
</body>
</html>
```